PELDRAX Business Cards

We require a business card for our company that provides IT consulting services. We already have a logo that needs to be used on the card. We want a clean professional looking design that incorporates our colours. Our main focus is providing managed services to business, which involves us looking after all of their IT requirements including managing servers/networks, projects, and procurement.

Industry/Entity Type

Information Technology

Requirements
Must have
• our logo, contact information, name, title, phone numbers

```html
<!DOCTYPE html>
<html lang="en">
<head>
<meta charset="utf-8">
<title>PELDRAX Business Cards</title>
<link href="https://fonts.googleapis.com/css2?family=Montserrat:wght@600&family=Arimo:wght@400;700&display=swap" rel="stylesheet">
<style>
  :root {
    --page-bg: #2b2b2d;
    --brand-blue: #1793d1;
    --map-blue: #5aaee0;
    --card-navy: #0b0d18;
    --text-white: #ffffff;
    --shadow: rgba(0, 0, 0, 0.55);
  }
  * { margin: 0; padding: 0; box-sizing: border-box; }
  html, body {
    width: 1200px;
    height: 1189px;
    overflow: hidden;
    background: var(--page-bg);
  }
  .sheet {
    position: relative;
    width: 1200px;
    height: 1189px;
  }
  .card {
    position: absolute;
    left: 210px;
    width: 780px;
    height: 446px;
    border-radius: 30px;
    box-shadow: 0 18px 40px var(--shadow);
    overflow: hidden;
  }
  .card--front {
    top: 110px;
    background: var(--brand-blue);
  }
  .card--back {
    top: 633px;
    background: var(--card-navy);
  }
  .map-area {
    position: absolute;
    left: 60px;
    top: 50px;
    width: 660px;
    height: 330px;
    border-radius: 46% 40% 44% 38%;
    background: radial-gradient(ellipse at center, rgba(90, 174, 224, 0.85) 0%, rgba(90, 174, 224, 0.45) 60%, rgba(90, 174, 224, 0) 78%);
  }
  .brand {
    position: absolute;
    display: flex;
    align-items: center;
    font-family: "Montserrat", sans-serif;
    font-weight: 600;
    white-space: nowrap;
  }
  .brand__dot {
    border-radius: 50%;
    flex: none;
  }
  .card--front .brand {
    left: 200px;
    top: 180px;
    gap: 18px;
    color: var(--text-white);
    font-size: 70px;
    letter-spacing: 6px;
  }
  .card--front .brand__dot {
    width: 62px;
    height: 62px;
    background: var(--text-white);
  }
  .card--back .brand {
    left: 50px;
    top: 226px;
    gap: 14px;
    color: var(--brand-blue);
    font-size: 40px;
    letter-spacing: 4px;
  }
  .card--back .brand__dot {
    width: 40px;
    height: 40px;
    background: var(--brand-blue);
  }
  .divider {
    position: absolute;
    left: 392px;
    top: 110px;
    width: 1px;
    height: 226px;
    background: var(--brand-blue);
  }
  .contact {
    position: absolute;
    left: 430px;
    top: 108px;
    font-family: "Arimo", sans-serif;
    color: var(--text-white);
  }
  .contact__name {
    font-weight: 700;
    font-size: 24px;
    color: var(--brand-blue);
    line-height: 1;
  }
  .contact__title {
    font-size: 16px;
    margin-top: 3px;
  }
  .contact__list {
    list-style: none;
    margin-top: 22px;
  }
  .contact__item {
    display: flex;
    align-items: center;
    gap: 10px;
    font-size: 16px;
    line-height: 1;
    margin-bottom: 7px;
    white-space: nowrap;
  }
  .contact__icon {
    width: 20px;
    height: 20px;
    flex: none;
  }
  .contact__address {
    font-size: 17px;
    line-height: 1.3;
    margin-top: 20px;
    font-style: normal;
  }
</style>
</head>
<body>
  <main class="sheet">
    <section class="card card--front">
      <div class="map-area" role="img" aria-label="Light blue world map silhouette"></div>
      <div class="brand"><span class="brand__dot"></span>PELDRAX</div>
    </section>

    <section class="card card--back">
      <div class="brand"><span class="brand__dot"></span>PELDRAX</div>
      <div class="divider"></div>
      <div class="contact">
        <p class="contact__name">Arlen Voss</p>
        <p class="contact__title">President &amp; CEO</p>
        <ul class="contact__list">
          <li class="contact__item">
            <svg class="contact__icon" viewBox="0 0 20 20"><circle cx="10" cy="10" r="9" fill="none" stroke="#1793d1" stroke-width="1.5"/><path d="M6 8c0-1.5 8-1.5 8 0v1h-2V8H8v1H6z M7 10h6l1 4H6z" fill="#1793d1"/></svg>
            +01 4821 7730 · desk@peldraxmail.com
          </li>
          <li class="contact__item">
            <svg class="contact__icon" viewBox="0 0 20 20"><circle cx="10" cy="10" r="9" fill="none" stroke="#1793d1" stroke-width="1.5"/><rect x="5" y="6.5" width="10" height="7" fill="#1793d1"/><path d="M5 6.5l5 4 5-4" fill="none" stroke="#0b0d18" stroke-width="1"/></svg>
            info@peldraxweb.com
          </li>
          <li class="contact__item">
            <svg class="contact__icon" viewBox="0 0 20 20"><circle cx="10" cy="10" r="9" fill="none" stroke="#1793d1" stroke-width="1.5"/><circle cx="10" cy="10" r="5" fill="none" stroke="#1793d1" stroke-width="1.2"/><ellipse cx="10" cy="10" rx="2.2" ry="5" fill="none" stroke="#1793d1" stroke-width="1"/><path d="M5 10h10" stroke="#1793d1" stroke-width="1"/></svg>
            www.peldraxweb.com
          </li>
        </ul>
        <address class="contact__address">PO BOX 480, Harrow Street<br>4th Lane, Leeds</address>
      </div>
    </section>
  </main>
</body>
</html>
```